Crowdsourced Research Platform: VELTA Polls

VELTA Polls is an acronym for Varied Estimates Linking Topical Attitudes (VELTA) Polls. This is a research effort to format and combine multiple sources of public opinion data from around the world into merged datasets. The website will at first mainly act as a quality control hub and distribution point for official dataset releases. It will provide resources such as codebooks, development guidelines, and instructional videos for crowdsourcing continued expansion of the resource. We need a coded (HTML and CSS) website design and associated files to launch the website with ease. We purchased the domain www.veltapolls.org, but access is blocked while it is under construction.

The website design should be based on a logo recently commissioned (see attached). The design should be simple and professional with lots of white space. We would like the logo on the top left of all pages and the primary navigation menu along the top-right of all pages. The primary navigation menu should have a simple mouse-over effect and the main menu items should expand with secondary drop-down options. The footer should include a few columns with headings and links to different pages. The website layout should be dynamic and expand its width to fit different sized screens. There will be a lot of data and information displayed in tables, so we would like the CSS coding and website design to include tables designed to match the website theme. The main graphical content will be data visualisations such as pie/bar charts, histograms, scatter plots, heat maps, moving average trend lines etc. We would therefore like the design to include modular sections (boxes matching theme to display plots/graphs/etc) that can visually display these types of figures with text/caption underneath to explain the data visualizations.

For more information and written placeholder content, designers should read the attached documents to get a better idea about the project. Some draft working papers using merged datsets have been included for reference and you can use these for their examples of data visualizations and use the written content for filling in page content.

Target Market(s)

The primary target audience will be academics in universities and research institutes. The resource will be most useful to quantitative social scientists, particularly political scientists and sociologists, but any discipline concerned with us humans could find the resource useful. Others such as graduate-level university students, civil servants in government departments, members of research institutions, and policy researchers in non-profit organizations will also find the resource useful.

Coding

Coded - Design and coding required

Number of Pages Required

3 page

Font styles to use
Sans Serif

Colors

Designer to choose colors to be used in the design.

Requirements
Must have
• HTML and CSS coding (not Wordpress)
Nice to have
• Content boxes to display data visualizations alongside articles.

```html
<!DOCTYPE html>
<html lang="en">
<head>
<meta charset="utf-8">
<title>VELTA Polls – Newsletter &amp; Footer</title>
<link rel="stylesheet" href="https://fonts.googleapis.com/css2?family=Arimo:wght@400;500&display=swap">
<style>
  :root {
    --ink: #1f1f24;
    --ink-soft: #6b6b74;
    --white: #ffffff;
    --field-bg: #f7f6fd;
    --violet: #9525ec;
    --violet-mid: #7a5fe0;
    --teal: #4fdad2;
    --teal-soft: #5fb4d8;
    --line-light: rgba(255, 255, 255, 0.45);
    --backdrop-left: #ae74e3;
    --backdrop-right: #6fd2cb;
  }
  * { box-sizing: border-box; margin: 0; padding: 0; }
  html, body {
    width: 1200px;
    height: 591px;
    overflow: hidden;
    font-family: "Arimo", Arial, sans-serif;
  }
  .canvas {
    position: relative;
    width: 1200px;
    height: 591px;
    overflow: hidden;
  }
  .backdrop {
    position: absolute;
    inset: 0;
    background: linear-gradient(100deg, var(--backdrop-left) 0%, #9d8ee0 45%, #7fb8dc 70%, var(--backdrop-right) 100%);
  }
  .page {
    position: absolute;
    left: 150px;
    top: 0;
    width: 900px;
    height: 591px;
  }

  /* Newsletter */
  .newsletter {
    position: absolute;
    left: 0;
    top: 0;
    width: 900px;
    height: 265px;
    background: var(--white);
    text-align: center;
  }
  .newsletter__title {
    position: absolute;
    top: 57px;
    left: 0;
    width: 100%;
    font-size: 20px;
    font-weight: 400;
    color: var(--ink);
  }
  .newsletter__tagline {
    position: absolute;
    top: 88px;
    left: 0;
    width: 100%;
    font-size: 12.5px;
    color: var(--ink-soft);
  }
  .subscribe {
    position: absolute;
    left: 239px;
    top: 131px;
    width: 418px;
    height: 44px;
    border-radius: 22px;
    background: var(--field-bg);
  }
  .subscribe__field {
    position: absolute;
    left: 23px;
    top: 0;
    line-height: 44px;
    font-size: 13px;
    color: #5c5c66;
  }
  .subscribe__button {
    position: absolute;
    right: 2px;
    top: 4px;
    width: 141px;
    height: 36px;
    border-radius: 18px;
    background: linear-gradient(90deg, var(--violet) 0%, var(--violet-mid) 50%, var(--teal) 100%);
    color: var(--white);
    font-size: 13px;
    line-height: 36px;
    text-align: left;
    padding-left: 27px;
  }
  .subscribe__button svg {
    position: absolute;
    right: 26px;
    top: 13px;
  }

  /* Footer */
  .site-footer {
    position: absolute;
    left: 0;
    top: 265px;
    width: 900px;
    height: 326px;
    background: linear-gradient(155deg, var(--violet) 0%, var(--violet-mid) 35%, var(--teal-soft) 70%, var(--teal) 100%);
    color: var(--white);
  }
  .contact-block {
    position: absolute;
    top: 89px;
  }
  .contact-block--about { left: 14px; }
  .contact-block--financials { left: 314px; }
  .contact-block--accreditation { left: 613px; }
  .contact-block__icon {
    position: absolute;
    left: 0;
    top: 0;
    width: 54px;
    height: 54px;
    border: 1px solid var(--line-light);
    display: flex;
    align-items: center;
    justify-content: center;
  }
  .contact-block__heading {
    position: absolute;
    left: 76px;
    top: 21px;
    font-size: 13px;
    font-weight: 400;
    white-space: nowrap;
    letter-spacing: 0.1px;
  }
  .contact-block__list {
    position: absolute;
    left: 76px;
    top: 58px;
    list-style: none;
    font-size: 13px;
    line-height: 19px;
    white-space: nowrap;
  }
  .site-footer__rule {
    position: absolute;
    left: 0;
    top: 271px;
    width: 900px;
    height: 1px;
    background: var(--line-light);
  }
  .site-footer__copyright {
    position: absolute;
    left: 14px;
    top: 291px;
    font-size: 13px;
  }
  .social-links {
    position: absolute;
    left: 769px;
    top: 285px;
    display: flex;
    gap: 4px;
    list-style: none;
  }
  .social-links__item {
    width: 27px;
    height: 27px;
    border: 1px solid rgba(255, 255, 255, 0.85);
  }
</style>
</head>
<body>
<div class="canvas">
  <div class="backdrop" role="img" aria-label="Background photograph of people using phones, tinted with a purple-to-teal overlay"></div>

  <main class="page">
    <section class="newsletter">
      <h2 class="newsletter__title">Subscribe for our Newsletter</h2>
      <p class="newsletter__tagline">Crowdsourced Research</p>
      <div class="subscribe">
        <span class="subscribe__field">Email address</span>
        <span class="subscribe__button">Get Started
          <svg width="13" height="10" viewBox="0 0 13 10" fill="none" stroke="#fff" stroke-width="1.1">
            <path d="M0 5h12M8 1l4 4-4 4"/>
          </svg>
        </span>
      </div>
    </section>

    <footer class="site-footer">
      <div class="contact-block contact-block--about">
        <div class="contact-block__icon">
          <svg width="22" height="22" viewBox="0 0 22 22" fill="none" stroke="#fff" stroke-width="1.1" stroke-linejoin="round">
            <path d="M13 2l7 7-2 1-3 3 0 4-1 1-4-4-6 6M13 2l-1 2-3 3-4 0-1 1 4 4"/>
          </svg>
        </div>
        <h3 class="contact-block__heading">ABOUT</h3>
        <ul class="contact-block__list">
          <li>Careers</li>
          <li>support@veltapolls.org</li>
        </ul>
      </div>

      <div class="contact-block contact-block--financials">
        <div class="contact-block__icon">
          <svg width="24" height="24" viewBox="0 0 24 24" fill="none" stroke="#fff" stroke-width="1.1">
            <circle cx="12" cy="12" r="10"/>
            <path d="M5 6c2 1 3 3 2 5 2 1 3 3 2 6M14 3c-1 2 0 3 2 4 1 2 3 2 4 2M15 21c0-3 2-4 3-6"/>
          </svg>
        </div>
        <h3 class="contact-block__heading">FINANCIALS</h3>
        <ul class="contact-block__list">
          <li>info@veltapolls.org</li>
          <li>support@veltapolls.org</li>
        </ul>
      </div>

      <div class="contact-block contact-block--accreditation">
        <div class="contact-block__icon">
          <svg width="26" height="22" viewBox="0 0 26 22" fill="none" stroke="#fff" stroke-width="1.1" stroke-linejoin="round">
            <path d="M2 8c0-4 5-6 11-6s11 2 11 6l-4 1-1-3H7L6 9z"/>
            <path d="M7 9l-3 10h18L19 9"/>
            <circle cx="13" cy="14" r="3"/>
          </svg>
        </div>
        <h3 class="contact-block__heading">ACCREDITATION</h3>
        <ul class="contact-block__list">
          <li>012 5550 104 2278</li>
          <li>012 5550 187 6634</li>
        </ul>
      </div>

      <div class="site-footer__rule"></div>
      <p class="site-footer__copyright">Copyright © 2018 | All rights reserved. VELTA Polls</p>
      <ul class="social-links" aria-label="Social profiles">
        <li class="social-links__item" aria-label="Social profile one"></li>
        <li class="social-links__item" aria-label="Social profile two"></li>
        <li class="social-links__item" aria-label="Social profile three"></li>
        <li class="social-links__item" aria-label="Social profile four"></li>
      </ul>
    </footer>
  </main>
</div>
</body>
</html>
```